Billboard design - consider what a billboard is

Design a billboard using my logo - Billboard is 6m x 3m
A Billboard is advertising for my company that is on a big sign.

Has to be clean and easy to read, and ideally highlights that we are Residential and Commercial builders.

Keep it clean and easy to read

The contact number for the board is

022 583 7092
www.harbourframeworks.co.nz
info@harbourframeworks.co.nz

Doesnt have to have all contact details if it doesnt fit

Has to catch peoples attention to contact us if they need a builder

Can you please change the sign to be all white writing, with black background ?
Updates

Please consider what a billboard is...

The design needs to be suitable for a billboard..

Target Market(s)

people driving past

Industry/Entity Type

Construction

Logo Text

Wellington Builder, website email address, contact number

Colors
0054AA
0677BA
7BADD7
CADEEF
E8F1F8

Requirements
Must have
• Easy to read
Nice to have
• easy to read, can clearly see contact details

```html
<!DOCTYPE html>
<html lang="en">
<head>
<meta charset="utf-8">
<title>Harbour Frameworks – Wellington Builder Billboard</title>
<link rel="stylesheet" href="https://fonts.googleapis.com/css2?family=Barlow+Condensed:wght@800&family=Montserrat:wght@700;800&display=swap">
<style>
  :root {
    --stage: #3b3a3c;
    --board: #000000;
    --brand-blue: #5a8bcc;
    --white: #ffffff;
  }
  * { margin: 0; padding: 0; box-sizing: border-box; }
  html, body {
    width: 1200px;
    height: 927px;
    overflow: hidden;
    background: var(--stage);
  }
  .billboard {
    position: absolute;
    left: 44px;
    top: 184px;
    width: 1114px;
    height: 558px;
    background: var(--board);
    overflow: hidden;
  }
  .billboard__art {
    position: absolute;
    inset: 0;
    width: 1114px;
    height: 558px;
  }
  .brand {
    position: absolute;
    left: 58px;
    top: 44px;
    display: flex;
    align-items: center;
    gap: 12px;
    font-family: "Montserrat", sans-serif;
    font-weight: 800;
    font-size: 34px;
    line-height: 1;
    color: var(--white);
  }
  .brand__mark {
    width: 26px;
    height: 26px;
    background: var(--brand-blue);
  }
  .services {
    position: absolute;
    left: 60px;
    top: 104px;
    font-family: "Montserrat", sans-serif;
    font-weight: 700;
    font-size: 24px;
    line-height: 1;
    letter-spacing: 2px;
    color: var(--white);
  }
  .headline__place {
    position: absolute;
    left: 58px;
    top: 176px;
    font-family: "Barlow Condensed", sans-serif;
    font-weight: 800;
    font-size: 100px;
    line-height: 1;
    letter-spacing: 2.5px;
    color: var(--white);
  }
  .headline__trade {
    position: absolute;
    left: 56px;
    top: 278px;
    font-family: "Montserrat", sans-serif;
    font-weight: 800;
    font-size: 104px;
    line-height: 1;
    letter-spacing: -3px;
    color: var(--white);
  }
  .divider {
    position: absolute;
    left: 60px;
    top: 395px;
    width: 412px;
    height: 4px;
    border-radius: 50%;
    background: var(--brand-blue);
  }
  .phone {
    position: absolute;
    left: 56px;
    top: 418px;
    font-family: "Montserrat", sans-serif;
    font-weight: 800;
    font-size: 70px;
    line-height: 1;
    letter-spacing: -1px;
    color: var(--white);
  }
  .web-band {
    position: absolute;
    left: 0;
    top: 505px;
    width: 1114px;
    height: 53px;
    background: var(--brand-blue);
    display: flex;
    align-items: center;
    justify-content: center;
    font-family: "Montserrat", sans-serif;
    font-weight: 800;
    font-size: 31px;
    color: var(--white);
    letter-spacing: -0.3px;
  }
</style>
</head>
<body>
  <section class="billboard">
    <svg class="billboard__art" viewBox="0 0 1114 558" xmlns="http://www.w3.org/2000/svg">
      <defs>
        <linearGradient id="house-tones" x1="0" y1="0" x2="0" y2="1">
          <stop offset="0" stop-color="#d8dde2"/>
          <stop offset="0.18" stop-color="#9a9aa0"/>
          <stop offset="0.32" stop-color="#3a3433"/>
          <stop offset="0.5" stop-color="#b78a5e"/>
          <stop offset="0.68" stop-color="#d0a777"/>
          <stop offset="0.8" stop-color="#7b7874"/>
          <stop offset="0.9" stop-color="#a9adb0"/>
          <stop offset="1" stop-color="#3f7294"/>
        </linearGradient>
      </defs>
      <path class="curve-accent" d="M636 0 C690 120 680 330 566 505 L1114 505 L1114 0 Z" fill="#5a8bcc"/>
      <path class="photo-area" role="img" aria-label="Photo of a modern two-storey glass home at dusk with warm interior lights, stone steps, sun loungers and a pool"
            d="M687 0 C720 150 700 360 581 505 L1114 505 L1114 0 Z" fill="url(#house-tones)"/>
    </svg>

    <div class="brand"><span class="brand__mark"></span>Harbour Frameworks</div>
    <p class="services">RESIDENTIAL &amp; COMMERCIAL</p>
    <h1 class="headline__place">WELLINGTON</h1>
    <h2 class="headline__trade">BUILDER</h2>
    <div class="divider"></div>
    <p class="phone">022 583 7092</p>
    <p class="web-band">www.harbourframeworks.co.nz</p>
  </section>
</body>
</html>
```